Webshop for furniture and lamps

We need a design for a web shop with APP that should have two options:
1-Webshop in general which should attract to private customer in general and
2-Website that is meant to attract big customers as hotels and restaurants who would have their own customerize login.

That's the idea behind the shop.

It should be diveded into 4 parts
vintage furniture
rattan set outdoor and indoor
lamps and
wooden wall decor

The name of the shop is borgo veneria!

Please kindly make me an offer.

Reason: Dear designers, so far there hasn't been a design that really matched. Look up German web sites like www.trevolind.de or www.quandor17.de... Haven't been convinced by designs! Sorry folks. Please submit some new ones. Kind regards Tam

```html
<!DOCTYPE html>
<html lang="en">
<head>
<meta charset="utf-8">
<title>Borgo Veneria – Furniture & Lamp</title>
<link rel="stylesheet" href="https://fonts.googleapis.com/css2?family=Roboto:wght@400;500;700&family=Lobster&display=swap">
<style>
:root{
  --red:#e24b45;
  --red-soft:rgba(232,98,92,.85);
  --yellow:#efb30a;
  --yellow-dark:#c98f00;
  --header-top:#474747;
  --header-bottom:#2a2a2a;
  --strip:#222;
  --panel:#4a4a4a;
  --banner-bg:#333;
  --footer:#1d1d1d;
  --footer-bar:#2b2b2b;
  --text-light:#f2f2f2;
  --text-muted:#b9b9b9;
  --white:#fff;
}
*{box-sizing:border-box;margin:0;padding:0}
html,body{width:786px;height:1200px;overflow:hidden;background:var(--footer)}
body{position:relative;font-family:"Roboto",sans-serif;color:var(--text-light)}
.abs{position:absolute}
.script{font-family:"Lobster",cursive;font-weight:400}

/* header */
.site-header{left:0;top:0;width:786px;height:112px;background:linear-gradient(var(--header-top),var(--header-bottom))}
.brand{left:117px;top:16px;font-size:16px;line-height:17px;letter-spacing:.5px;color:var(--white);font-weight:400;text-transform:uppercase}
.account{left:373px;top:27px;font-size:7px;color:var(--text-muted)}
.search{left:478px;top:21px;width:99px;height:19px;display:flex}
.search span{flex:1;background:var(--white);color:#555;font-size:7px;padding:5px 5px}
.search i{width:19px;background:var(--red);display:flex;align-items:center;justify-content:center}
.round-btn{top:20px;width:21px;height:21px;border-radius:50%;background:var(--red);display:flex;align-items:center;justify-content:center}
.cart-label{left:641px;top:26px;font-size:9px;font-weight:700}
.main-nav{left:116px;top:66px;width:560px;height:27px;border-top:1px solid #666;border-bottom:1px solid #666;display:flex;align-items:center;justify-content:space-between;font-size:9px;color:var(--white)}
.main-nav .active{color:var(--red)}

/* hero */
.hero{left:0;top:112px;width:786px;height:313px;background:linear-gradient(90deg,#5b5d63 0%,#6d6c6e 30%,#9b7156 34%,#b88a66 60%,#c39a78 100%)}
.hero-bed{left:330px;top:225px;width:456px;height:200px;background:linear-gradient(#ece4d6,#cfc3b0)}
.hero-title{left:277px;top:210px;font-size:25px;font-weight:500;color:var(--white);text-shadow:0 1px 3px rgba(0,0,0,.5);line-height:36px}
.hero-title b{font-size:29px;font-weight:500;display:block}
.buy-now{left:280px;top:289px;width:93px;height:32px;border-radius:3px;background:var(--red);box-shadow:0 2px 0 #a8322e;font-size:13px;display:flex;align-items:center;justify-content:center;color:var(--white)}

/* category strip */
.strip{left:0;top:425px;width:786px;height:156px;background:var(--strip)}
.tile{top:437px;width:182px;height:128px;border:2px solid var(--white);overflow:hidden}
.tile .ph{position:absolute;inset:0}
.tile .cap{position:absolute;left:0;right:0;bottom:0;height:22px;background:rgba(60,60,60,.85);display:flex;align-items:center;justify-content:space-between;padding:0 8px;font-size:11px}

/* feature grid */
.features{left:0;top:581px;width:786px;height:273px;background:var(--panel)}
.card{width:277px;height:109px;border:2px solid var(--white);overflow:hidden}
.card .ph{position:absolute;inset:0}
.card .band{position:absolute;left:0;right:0;top:0;height:22px;background:var(--red-soft);padding:3px 10px;font-size:12px}
.shop-now{position:absolute;height:21px;padding:0 8px;border-radius:2px;background:linear-gradient(#f6c42b,var(--yellow));box-shadow:0 2px 0 var(--yellow-dark);font-size:8.5px;font-weight:500;display:flex;align-items:center;gap:6px;color:var(--white)}

/* banner */
.banner-wrap{left:0;top:854px;width:786px;height:157px;background:var(--banner-bg)}
.banner{left:115px;top:862px;width:560px;height:135px;border:2px solid var(--white);background:linear-gradient(90deg,#3d5b6b 0%,#a2514a 30%,#7b6d60 55%,#b3a596 75%,#c7bdb0 100%)}
.banner-kicker{left:451px;top:890px;font-size:16px}
.banner-title{left:451px;top:910px;font-size:28px;text-shadow:0 1px 2px rgba(0,0,0,.4)}

/* footer */
.site-footer{left:0;top:1011px;width:786px;height:142px;background:var(--footer)}
.footer-col h3{font-size:11.5px;font-weight:400;color:var(--white);margin-bottom:11px}
.footer-col p,.footer-col li{font-size:7px;line-height:13.5px;color:var(--text-muted);list-style:none}
.about p{text-align:justify;width:111px}
.email-field{width:132px;height:18px;display:flex;margin-top:4px}
.email-field span{flex:1;background:var(--white);color:#777;font-size:6.5px;padding:5px 4px}
.email-field i{width:18px;background:var(--red);display:flex;align-items:center;justify-content:center}
.social{display:flex;gap:5px;margin-top:6px}
.social span{width:19px;height:19px;border-radius:50%;border:2px solid var(--white)}
.footer-bar{left:0;top:1153px;width:786px;height:47px;background:var(--footer-bar)}
.pay{top:1168px;width:28px;height:16px;border-radius:2px}
.copyright{left:542px;top:1172px;font-size:8px;color:var(--white)}
</style>
</head>
<body>

<header class="site-header abs">
  <div class="brand abs">Borgo<br>Veneria</div>
  <div class="account abs">Log in &nbsp;or&nbsp; Create an account</div>
  <div class="search abs"><span>Search</span><i><svg width="9" height="9" viewBox="0 0 10 10"><circle cx="4" cy="4" r="3" fill="none" stroke="#fff" stroke-width="1.4"/><path d="M6.3 6.3 9 9" stroke="#fff" stroke-width="1.4"/></svg></i></div>
  <div class="round-btn abs" style="left:588px"><svg width="9" height="10" viewBox="0 0 9 10"><rect x="0.5" y="2.5" width="5" height="7" fill="none" stroke="#fff"/><rect x="3" y="0.5" width="5" height="7" fill="#fff"/></svg></div>
  <div class="round-btn abs" style="left:615px"><svg width="11" height="9" viewBox="0 0 11 9"><path d="M1 2h9l-1.3 5H2.3z" fill="#fff"/><path d="M3 2 5 0M8 2 6 0" stroke="#fff"/></svg></div>
  <div class="cart-label abs">Cart (0)</div>
  <nav class="main-nav abs">
    <span class="active">HOME</span><span>|</span><span>ABOUT US</span><span>|</span><span>SERVICES</span><span>|</span><span>PRODUCTS</span><span>|</span><span>CUSTOMERS</span><span>|</span><span>BLOG</span><span>|</span><span>NEWS</span><span>|</span><span>CONTACT US</span>
  </nav>
</header>

<section class="hero abs" role="img" aria-label="Bedroom interior with a wooden block wall, a cream bed and a white side cabinet">
</section>
<div class="hero-bed abs" aria-hidden="true"></div>
<svg class="abs" style="left:66px;top:232px" width="20" height="44" viewBox="0 0 20 44" aria-hidden="true"><path d="M19 1 1 22l18 21" fill="none" stroke="#fff" stroke-width="1.3"/></svg>
<svg class="abs" style="left:700px;top:232px" width="20" height="44" viewBox="0 0 20 44" aria-hidden="true"><path d="M1 1l18 21L1 43" fill="none" stroke="#fff" stroke-width="1.3"/></svg>
<h1 class="hero-title abs">BORGO VENERIA<b>FURNITURE &amp; LAMP</b></h1>
<div class="buy-now abs">BUY NOW</div>

<section class="strip abs"></section>
<div class="tile abs" style="left:115px">
  <div class="ph" role="img" aria-label="Wooden wall cabinet with painted tiles" style="background:linear-gradient(135deg,#e8e4df,#7b5a3f 55%,#e9e6e2)"></div>
  <div class="cap"><span class="script">Wooden wall decor</span><svg width="7" height="12" viewBox="0 0 7 12"><path d="M1 1l5 5-5 5" fill="none" stroke="#fff" stroke-width="1.3"/></svg></div>
</div>
<div class="tile abs" style="left:303px">
  <div class="ph" role="img" aria-label="Brass floor lamp with cream shade" style="background:linear-gradient(#f6f4ef,#f2d999 30%,#fbfaf6 45%,#fff)"></div>
  <div class="cap"><span class="script">Lamps</span><svg width="7" height="12" viewBox="0 0 7 12"><path d="M1 1l5 5-5 5" fill="none" stroke="#fff" stroke-width="1.3"/></svg></div>
</div>
<div class="tile abs" style="left:491px">
  <div class="ph" role="img" aria-label="Round rattan outdoor table set" style="background:linear-gradient(#fff,#5a5654 45%,#3f3b39 75%,#fff)"></div>
  <div class="cap"><span class="script">Rattan set outdoor</span><svg width="7" height="12" viewBox="0 0 7 12"><path d="M1 1l5 5-5 5" fill="none" stroke="#fff" stroke-width="1.3"/></svg></div>
</div>

<section class="features abs"></section>
<article class="card abs" style="left:115px;top:605px">
  <div class="ph" role="img" aria-label="Rattan garden sofa and table in a garden" style="background:linear-gradient(#d98f63,#7a8a4a 35%,#a48d6c 60%,#8c8a82)"></div>
  <div class="band script">Vintage furniture</div>
  <div class="shop-now" style="left:182px;top:80px">SHOP NOW <svg width="5" height="9" viewBox="0 0 5 9"><path d="M.5.5l4 4-4 4" fill="none" stroke="#fff"/></svg></div>
</article>
<article class="card abs" style="left:398px;top:605px">
  <div class="ph" role="img" aria-label="Black rattan dining set with glass table" style="background:linear-gradient(#b45c4f,#3c3a3b 35%,#8a8f94 55%,#2e2c2d)"></div>
  <div class="band script">Rattan set outdoor</div>
  <div class="shop-now" style="left:188px;top:80px">SHOP NOW <svg width="5" height="9" viewBox="0 0 5 9"><path d="M.5.5l4 4-4 4" fill="none" stroke="#fff"/></svg></div>
</article>
<article class="card abs" style="left:115px;top:721px">
  <div class="ph" role="img" aria-label="Orange lamp shade on a brass stand" style="background:linear-gradient(#f1f1f1,#e8552b 45%,#f4f4f4 60%,#fff)"></div>
  <div class="band script">Lamps</div>
  <div class="shop-now" style="left:188px;top:78px">SHOP NOW <svg width="5" height="9" viewBox="0 0 5 9"><path d="M.5.5l4 4-4 4" fill="none" stroke="#fff"/></svg></div>
</article>
<article class="card abs" style="left:398px;top:721px">
  <div class="ph" role="img" aria-label="Painted reclaimed wood cabinet top" style="background:linear-gradient(135deg,#d6cabd,#b84a3e 35%,#5d7a6a 55%,#5a3b2a 80%,#cdbfae)"></div>
  <div class="band script">Wooden wall decor</div>
  <div class="shop-now" style="left:188px;top:79px">SHOP NOW <svg width="5" height="9" viewBox="0 0 5 9"><path d="M.5.5l4 4-4 4" fill="none" stroke="#fff"/></svg></div>
</article>

<section class="banner-wrap abs"></section>
<div class="banner abs" role="img" aria-label="Close-up of a vintage painted tin sign on a wooden cabinet"></div>
<div class="banner-kicker abs script">Borgo Veneria</div>
<div class="banner-title abs script">Vintage furniture</div>
<div class="shop-now abs" style="left:560px;top:958px">SHOP NOW <svg width="5" height="9" viewBox="0 0 5 9"><path d="M.5.5l4 4-4 4" fill="none" stroke="#fff"/></svg></div>

<footer class="site-footer abs">
  <div class="footer-col about abs" style="left:112px;top:27px">
    <h3 style="margin-left:3px">ABOUT US</h3>
    <p>Lorem Ipsum has been the industry's standard dummy text ever since the 1500s, when an unknown printer took a galley of type and scrambled it to make a type specimen book.</p>
  </div>
  <div class="footer-col abs" style="left:247px;top:27px">
    <h3>CONTACT US</h3>
    <ul style="margin-left:3px"><li>Borgo Veneria Ltd</li><li>18 Via dei Tigli</li><li>&nbsp;Verona</li><li>Tel 0162-884-307</li><li>Email sales@borgoveneria.shop</li></ul>
  </div>
  <div class="footer-col abs" style="left:390px;top:27px">
    <h3>INFORMATION</h3>
    <ul style="margin-left:1px"><li>Specials</li><li>Our store(s)!</li><li>Contact us</li><li>Terms and conditions of use</li><li>About us</li></ul>
  </div>
  <div class="footer-col abs" style="left:543px;top:27px">
    <h3>NEWSLETTER</h3>
    <p>Sign Up for Our Newsletter:</p>
    <div class="email-field"><span>Email</span><i><svg width="6" height="10" viewBox="0 0 6 10"><path d="M1 1l4 4-4 4" fill="none" stroke="#fff" stroke-width="1.3"/></svg></i></div>
    <p style="margin-top:9px">Follow us on:</p>
    <div class="social"><span style="background:#3b5998"></span><span style="background:#dd4b39"></span><span style="background:#2aa3e0"></span><span style="background:#f26522"></span></div>
  </div>
</footer>

<div class="footer-bar abs"></div>
<div class="pay abs" style="left:114px;background:#2b4da0;border-bottom:3px solid #f2a900"></div>
<div class="pay abs" style="left:148px;background:#c5362c"></div>
<div class="pay abs" style="left:182px;background:#3f7fc4"></div>
<div class="copyright abs">Copyright © 2014 &nbsp;All rights reserved.</div>

</body>
</html>
```